Bluefern Capital Counsel Needs a Letterhead

Tomi, we need a letterhead/banner for our blog, which is titled "Quiet Harbor Chronicle". The letterhead/banner should incorporate the enclosed banner image, logo, and the name of our blog ("Quiet Harbor Chronicle").

We would also like an alternative design that includes our picture. Here, we have two options that we would like to see.

In all, we would like to see 3 different designs: one banner without any pics; and two banner with two versions of our pictures.

The file size should be able to be resized for the space given to us at our website (http://bluefern-capital-counsel.com).

We also need the letterhead/banner by Friday, June 13. Thanks!!

```html
<!DOCTYPE html>
<html lang="en">
<head>
<meta charset="utf-8">
<title>Quiet Harbor Chronicle — Blog Banner</title>
<link rel="stylesheet" href="https://fonts.googleapis.com/css2?family=Bebas+Neue&family=Oswald:wght@400&display=swap">
<style>
  :root {
    --paper-light: #f8f3b4;
    --paper-mid: #efe89c;
    --paper-deep: #e2da86;
    --ink: #0d0d0d;
    --brand-panel: #141210;
    --brand-text: #efe9a8;
  }
  * { margin: 0; padding: 0; box-sizing: border-box; }
  html, body {
    width: 1200px;
    height: 250px;
    overflow: hidden;
    background: #ffffff;
  }
  .banner {
    position: relative;
    width: 1200px;
    height: 250px;
    overflow: hidden;
  }
  .banner__backdrop {
    position: absolute;
    inset: 0;
    background:
      radial-gradient(ellipse at 70% 40%, var(--paper-light) 0%, transparent 60%),
      linear-gradient(100deg, var(--paper-mid) 0%, var(--paper-light) 45%, var(--paper-mid) 75%, var(--paper-deep) 100%);
  }
  .brand-panel {
    position: absolute;
    left: 22px;
    top: 22px;
    width: 278px;
    height: 200px;
    background: var(--brand-panel);
    display: flex;
    align-items: flex-end;
    justify-content: center;
    padding-bottom: 30px;
  }
  .brand-panel__name {
    font-family: "Oswald", "Arial Narrow", sans-serif;
    font-weight: 400;
    font-size: 24px;
    line-height: 1.1;
    color: var(--brand-text);
    text-align: center;
    letter-spacing: 0.2px;
  }
  .blog-title {
    position: absolute;
    left: 328px;
    top: 26px;
    font-family: "Bebas Neue", "Impact", sans-serif;
    font-weight: 400;
    font-size: 118px;
    line-height: 104px;
    color: var(--ink);
    letter-spacing: 1px;
    white-space: nowrap;
  }
  .blog-title span { display: block; }
</style>
</head>
<body>
  <header class="banner">
    <div class="banner__backdrop" role="img" aria-label="Yellow-tinted photo of a handwritten cheque and a pen on a desk"></div>

    <div class="brand-panel">
      <p class="brand-panel__name">Bluefern Capital Counsel</p>
    </div>

    <h1 class="blog-title">
      <span>Quiet Harbor</span>
      <span>Chronicle</span>
    </h1>
  </header>
</body>
</html>
```